Retail swing tag labels for a sale / reduction

We need some graphics done to be made into retail swing tag labels, for the purpose of reductions on selected products.

We have attached 2 examples of previous designs that were similar idea, but more themed for 'autumn' and 'winter'. This theme will just have the word 'REDUCED'.

The white areas can be smaller in size, as we would like to include a large "20% OFF" at the bottom, and then a 30%, 40%, 50% option.

Overall colour scheme should be red background with some form of detailed patterning (see previous examples). Bright and e-catching.

Any other questions, just ask.

The screenshot is front the printers, but in horizontal orientation.

The finished dimensions will be A6 portrait, printed both sides.

We have also included the vector file of the shop "Hallmere Furnishings", which can be included on 1 of the sides.

```html
<!DOCTYPE html>
<html lang="en">
<head>
<meta charset="utf-8">
<title>Hallmere Furnishings – Reduced Swing Tag</title>
<link rel="stylesheet" href="https://fonts.googleapis.com/css2?family=Bebas+Neue&family=Oswald:wght@500;600&family=Raleway:wght@400&family=Open+Sans:wght@400&display=swap">
<style>
  :root {
    --page: #ffffff;
    --red-bright: #e0262e;
    --red-mid: #c0141c;
    --red-deep: #5e0408;
    --red-mottle: rgba(90, 0, 6, 0.45);
    --red-glow: rgba(240, 50, 58, 0.55);
    --ink-shadow: rgba(60, 0, 4, 0.42);
    --white: #ffffff;
    --label: #111111;
  }
  html, body {
    margin: 0;
    padding: 0;
    width: 1200px;
    height: 940px;
    overflow: hidden;
    background: var(--page);
  }
  .sheet {
    position: relative;
    width: 1200px;
    height: 940px;
    margin: 0;
  }
  .tag {
    position: absolute;
    top: 74px;
    width: 508px;
    height: 718px;
    overflow: hidden;
    background:
      radial-gradient(circle at 12% 8%, var(--red-mottle) 0%, transparent 22%),
      radial-gradient(circle at 78% 18%, var(--red-glow) 0%, transparent 18%),
      radial-gradient(circle at 30% 35%, var(--red-mottle) 0%, transparent 15%),
      radial-gradient(circle at 85% 52%, var(--red-mottle) 0%, transparent 16%),
      radial-gradient(circle at 22% 62%, var(--red-glow) 0%, transparent 17%),
      radial-gradient(circle at 60% 78%, var(--red-mottle) 0%, transparent 14%),
      radial-gradient(circle at 10% 92%, var(--red-mottle) 0%, transparent 20%),
      radial-gradient(circle at 90% 95%, var(--red-mottle) 0%, transparent 18%),
      radial-gradient(ellipse at 55% 45%, var(--red-bright) 0%, var(--red-mid) 55%, var(--red-deep) 100%);
  }
  .tag--front { left: 66px; }
  .tag--back  { left: 624px; }

  .tag__watermark {
    position: absolute;
    inset: 0;
    width: 508px;
    height: 718px;
  }
  .tag__watermark text {
    font-family: "Bebas Neue", "Oswald", sans-serif;
    fill: var(--ink-shadow);
  }

  .brand {
    position: absolute;
    left: 0;
    top: 64px;
    width: 508px;
    text-align: center;
  }
  .brand__square {
    display: block;
    width: 92px;
    height: 92px;
    margin: 0 auto;
    border: 1.5px solid var(--white);
    box-sizing: border-box;
  }
  .brand__name {
    display: block;
    margin-top: 16px;
    font-family: "Raleway", sans-serif;
    font-weight: 400;
    font-size: 27px;
    line-height: 32px;
    letter-spacing: 4.5px;
    color: var(--white);
    text-transform: uppercase;
  }

  .badge {
    position: absolute;
    left: 100px;
    top: 296px;
    width: 280px;
    height: 280px;
  }
  .badge__ring-text {
    font-family: "Oswald", sans-serif;
    font-weight: 500;
    font-size: 15px;
    letter-spacing: 7px;
    fill: var(--red-mid);
  }
  .badge__figure {
    font-family: "Oswald", sans-serif;
    font-weight: 600;
    fill: var(--white);
  }

  .price-box {
    position: absolute;
    left: 47px;
    width: 414px;
    box-sizing: border-box;
    border: 4px solid var(--white);
    border-radius: 13px;
    color: var(--white);
    text-align: center;
    font-family: "Bebas Neue", "Oswald", sans-serif;
  }
  .price-box--was {
    top: 258px;
    height: 102px;
    font-size: 78px;
    line-height: 96px;
    letter-spacing: 1px;
  }
  .price-box--now {
    top: 386px;
    height: 292px;
  }
  .price-box__heading {
    display: flex;
    align-items: center;
    justify-content: center;
    gap: 16px;
    margin-top: 14px;
    font-size: 84px;
    line-height: 80px;
  }
  .price-box__rule {
    display: block;
    width: 100px;
    height: 3px;
    background: var(--white);
  }
  .price-box__amount {
    display: block;
    margin-top: 14px;
    font-size: 194px;
    line-height: 172px;
    letter-spacing: 4px;
  }

  .side-label {
    position: absolute;
    top: 820px;
    width: 508px;
    margin: 0;
    text-align: center;
    font-family: "Open Sans", sans-serif;
    font-size: 46px;
    line-height: 64px;
    color: var(--label);
  }
  .side-label--front { left: 66px; }
  .side-label--back  { left: 624px; }
</style>
</head>
<body>
<main class="sheet">

  <section class="tag tag--front">
    <svg class="tag__watermark" viewBox="0 0 508 718" aria-hidden="true">
      <g transform="translate(0,0) scale(1,-1)">
        <text x="14" y="0" font-size="290" textLength="480" lengthAdjust="spacingAndGlyphs">REDUCED</text>
      </g>
      <text x="14" y="445" font-size="330" textLength="480" lengthAdjust="spacingAndGlyphs">REDUCED</text>
      <g transform="translate(0,458) scale(1,-1)">
        <text x="14" y="0" font-size="380" textLength="480" lengthAdjust="spacingAndGlyphs">REDUCED</text>
      </g>
    </svg>

    <div class="brand">
      <span class="brand__square"></span>
      <span class="brand__name">Hallmere Furnishings</span>
    </div>

    <svg class="badge" viewBox="-140 -140 280 280" role="img" aria-label="Special offer, 30% off">
      <defs>
        <path id="spike" d="M-14.6,-111 L0,-136 L14.6,-111 Z"/>
        <path id="arc-top" d="M-91,0 A91,91 0 0 1 91,0"/>
        <path id="arc-bottom" d="M-100,0 A100,100 0 0 0 100,0"/>
      </defs>
      <g fill="var(--white)">
        <circle r="114"/>
        <use href="#spike" transform="rotate(0)"/>
        <use href="#spike" transform="rotate(15)"/>
        <use href="#spike" transform="rotate(30)"/>
        <use href="#spike" transform="rotate(45)"/>
        <use href="#spike" transform="rotate(60)"/>
        <use href="#spike" transform="rotate(75)"/>
        <use href="#spike" transform="rotate(90)"/>
        <use href="#spike" transform="rotate(105)"/>
        <use href="#spike" transform="rotate(120)"/>
        <use href="#spike" transform="rotate(135)"/>
        <use href="#spike" transform="rotate(150)"/>
        <use href="#spike" transform="rotate(165)"/>
        <use href="#spike" transform="rotate(180)"/>
        <use href="#spike" transform="rotate(195)"/>
        <use href="#spike" transform="rotate(210)"/>
        <use href="#spike" transform="rotate(225)"/>
        <use href="#spike" transform="rotate(240)"/>
        <use href="#spike" transform="rotate(255)"/>
        <use href="#spike" transform="rotate(270)"/>
        <use href="#spike" transform="rotate(285)"/>
        <use href="#spike" transform="rotate(300)"/>
        <use href="#spike" transform="rotate(315)"/>
        <use href="#spike" transform="rotate(330)"/>
        <use href="#spike" transform="rotate(345)"/>
      </g>
      <text class="badge__ring-text" text-anchor="middle"><textPath href="#arc-top" startOffset="50%">SPECIAL</textPath></text>
      <text class="badge__ring-text" text-anchor="middle"><textPath href="#arc-bottom" startOffset="50%">OFFER</textPath></text>
      <circle r="86" fill="var(--red-mid)"/>
      <rect x="-120" y="-20" width="58" height="40" fill="var(--white)"/>
      <rect x="62" y="-20" width="58" height="40" fill="var(--white)"/>
      <circle r="76" fill="var(--red-mid)" stroke="var(--white)" stroke-width="4"/>
      <text class="badge__figure" x="10" y="24" font-size="60" text-anchor="end">30</text>
      <text class="badge__figure" x="13" y="-2" font-size="32">%</text>
      <text class="badge__figure" x="13" y="24" font-size="21">OFF</text>
    </svg>
  </section>

  <section class="tag tag--back">
    <svg class="tag__watermark" viewBox="0 0 508 718" aria-hidden="true">
      <g transform="translate(0,0) scale(1,-1)">
        <text x="14" y="0" font-size="290" textLength="480" lengthAdjust="spacingAndGlyphs">REDUCED</text>
      </g>
      <text x="14" y="445" font-size="330" textLength="480" lengthAdjust="spacingAndGlyphs">REDUCED</text>
      <g transform="translate(0,458) scale(1,-1)">
        <text x="14" y="0" font-size="380" textLength="480" lengthAdjust="spacingAndGlyphs">REDUCED</text>
      </g>
    </svg>

    <div class="brand">
      <span class="brand__square"></span>
      <span class="brand__name">Hallmere Furnishings</span>
    </div>

    <div class="price-box price-box--was">WAS £ 4.99</div>

    <div class="price-box price-box--now">
      <div class="price-box__heading">
        <span class="price-box__rule"></span>
        <span>NOW</span>
        <span class="price-box__rule"></span>
      </div>
      <span class="price-box__amount">£1.99</span>
    </div>
  </section>

  <p class="side-label side-label--front">front</p>
  <p class="side-label side-label--back">back</p>

</main>
</body>
</html>
```